Business Cards - Bright Trim Yard (Cleaning, Handyman & Mowing Business)
Bright Trim Yard
Business Cards - Bright Trim Yard (Cleaning, Handyman & Mowing Business) - Trade
Creative Brief
Professional
PO Box 318 Galloway Rise, QLD, 4127
0412 GO TIDY (0412 46 8439) should these 2 versions of the number be put on a separate line?
contact@brighttrimyard.com.au
www.brighttrimyard.com.au
ABN: 38 916 204 571
Cards are to be generic and not have a persons name or title, only a business card for the business itself.
Will consider ideas or suggestions from designers - maybe a full size logo, maybe a special offer for "refer a friend who makes a booking and receive 25% off your next service" or similar, maybe both logo and text at bottom with refer a friend offer.

```html
<!DOCTYPE html>
<html lang="en">
<head>
<meta charset="utf-8">
<title>Bright Trim Yard – Business Cards</title>
<link href="https://fonts.googleapis.com/css2?family=Nunito:wght@400;600;800&display=swap" rel="stylesheet">
<style>
  :root {
    --backdrop: #ecebe7;
    --card: #ffffff;
    --brand-blue: #2a9fd8;
    --brand-green: #7dbb2a;
    --accent-orange: #f2a21a;
    --text-grey: #6d6f72;
    --tagline-navy: #1f5f8f;
    --bubble-light: #eef6fc;
    --bubble-mid: #d7eaf8;
  }
  * { box-sizing: border-box; margin: 0; padding: 0; }
  html, body {
    width: 1200px;
    height: 1023px;
    overflow: hidden;
    background: var(--backdrop);
    font-family: "Nunito", sans-serif;
  }
  .sheet {
    position: relative;
    width: 1200px;
    height: 1023px;
  }
  .card {
    position: absolute;
    left: 220px;
    width: 760px;
    height: 434px;
    background: var(--card);
    border-radius: 18px;
    overflow: hidden;
    box-shadow: 0 10px 30px rgba(0,0,0,0.12);
  }
  .card--front { top: 52px; }
  .card--back { top: 537px; }

  /* Front */
  .front-edge {
    position: absolute;
    left: 0; right: 0; bottom: 0;
    height: 18px;
    background: var(--accent-orange);
  }
  .brand {
    position: absolute;
    left: 40px;
    top: 150px;
  }
  .brand__mark {
    font-weight: 800;
    font-size: 32px;
    color: var(--brand-blue);
    letter-spacing: -0.3px;
  }
  .brand__name {
    margin-top: 26px;
    font-weight: 400;
    font-size: 24px;
    color: var(--brand-blue);
  }
  .details {
    position: absolute;
    left: 360px;
    top: 78px;
    padding-left: 20px;
    border-left: 3px solid var(--brand-green);
    display: grid;
    grid-template-columns: 90px 270px;
    row-gap: 10px;
    font-size: 15px;
    line-height: 1.4;
  }
  .details__label {
    color: var(--brand-green);
    font-weight: 600;
  }
  .details__value { color: var(--text-grey); }

  /* Back */
  .bubble-field {
    position: absolute;
    inset: 0;
    background: radial-gradient(circle at 30% 35%, var(--bubble-mid) 0%, var(--bubble-light) 55%, var(--card) 100%);
  }
  .back-lockup {
    position: absolute;
    inset: 0;
    display: flex;
    flex-direction: column;
    align-items: center;
    justify-content: center;
  }
  .back-lockup__mark {
    font-weight: 800;
    font-size: 60px;
    color: var(--brand-blue);
    letter-spacing: -0.5px;
  }
  .back-lockup__tagline {
    margin-top: 14px;
    font-weight: 600;
    font-size: 26px;
    color: var(--tagline-navy);
    letter-spacing: 1px;
  }
</style>
</head>
<body>
<main class="sheet">
  <section class="card card--front" aria-label="Business card front">
    <div class="brand">
      <div class="brand__mark">Bright Trim Yard</div>
      <div class="brand__name">Bright Trim Yard</div>
    </div>
    <dl class="details">
      <dt class="details__label">Address</dt>
      <dd class="details__value">PO Box 318<br>Galloway Rise, QLD, 4127</dd>
      <dt class="details__label">Phone</dt>
      <dd class="details__value">0412 GO TIDY<br>0412 46 8439</dd>
      <dt class="details__label">Email</dt>
      <dd class="details__value">contact@brighttrimyard.com.au</dd>
      <dt class="details__label">Website</dt>
      <dd class="details__value">www.brighttrimyard.com.au</dd>
      <dt class="details__label">ABN</dt>
      <dd class="details__value">38 916 204 571</dd>
    </dl>
    <div class="front-edge"></div>
  </section>

  <section class="card card--back" aria-label="Business card back">
    <div class="bubble-field" role="img" aria-label="Soft light-blue bubble pattern background"></div>
    <div class="back-lockup">
      <div class="back-lockup__mark">Bright Trim Yard</div>
      <div class="back-lockup__tagline">Tidy Homes. Sharp Yards.</div>
    </div>
  </section>
</main>
</body>
</html>
```